Composite decking sales poster

Poster advertising our brand of decking and our industry-best warranty.
Poster dimensions 1200mm wide x 400mm high.
50 Year Stain and Fade Warranty.
Ultra-Low Maintenance.
Environmentally Friendly Made from Recycled Materials.
Website: https://velmorboards.com.au
Phone: 1300 482 937
*** Uploaded pictures are optional to use ***
Must list website, phone number and logos.

```html
<!DOCTYPE html>
<html lang="en">
<head>
<meta charset="utf-8">
<title>Velmor Boards – Composite Decking Poster</title>
<link rel="stylesheet" href="https://fonts.googleapis.com/css2?family=Rubik:ital,wght@0,300;0,400;0,600;0,700;1,800&display=swap">
<style>
  :root {
    --backdrop: #2a2a2a;
    --brand-blue: #4d73a0;
    --ink-dark: #3e3e3e;
    --white: #ffffff;
    --wood-dark: #2f2119;
    --wood-mid: #6b4631;
    --wood-light: #a06f4f;
    --badge-grey: #6d655e;
  }
  * { margin: 0; padding: 0; box-sizing: border-box; }
  html, body { width: 1200px; height: 445px; overflow: hidden; background: var(--backdrop); }
  body { font-family: "Rubik", sans-serif; color: var(--white); }

  .poster {
    position: absolute; left: 38px; top: 37px; width: 1130px; height: 376px; overflow: hidden;
    box-shadow: 0 6px 10px rgba(0,0,0,.45);
  }
  .deck-photo {
    position: absolute; inset: 0;
    background:
      radial-gradient(ellipse at 80% 10%, rgba(60,80,50,.8) 0%, rgba(60,80,50,0) 35%),
      linear-gradient(160deg, var(--wood-light) 0%, var(--wood-mid) 30%, var(--wood-dark) 60%, var(--wood-mid) 85%, var(--wood-light) 100%);
  }
  .shapes { position: absolute; inset: 0; }

  .brand { position: absolute; left: 16px; top: 34px; display: flex; align-items: center; gap: 10px; }
  .brand-mark { width: 30px; height: 30px; background: var(--brand-blue); }
  .brand-name { font-weight: 600; font-size: 30px; color: var(--ink-dark); letter-spacing: -.3px; }

  .website { position: absolute; right: 22px; top: 17px; display: flex; align-items: center; gap: 8px; font-size: 17px; letter-spacing: .4px; }
  .website svg { width: 25px; height: 25px; }

  .pill {
    position: absolute; background: var(--brand-blue); border-radius: 24px;
    display: flex; align-items: center; justify-content: center; white-space: nowrap;
  }
  .pill strong { font-weight: 700; margin-right: 8px; }
  .pill span { font-weight: 300; }
  .pill-maintenance { left: 283px; top: 107px; width: 342px; height: 43px; font-size: 26px; }
  .pill-eco { left: 161px; top: 160px; width: 585px; height: 43px; font-size: 21px; }
  .pill-phone { left: 329px; top: 289px; width: 272px; height: 47px; font-size: 31px; font-weight: 700; gap: 8px; }
  .pill-phone svg { width: 26px; height: 26px; }

  .headline { position: absolute; left: 68px; top: 214px; font-size: 46px; white-space: nowrap; letter-spacing: .3px; }
  .headline em { font-style: italic; font-weight: 800; margin-right: 10px; }
  .headline span { font-weight: 300; }

  .badge {
    position: absolute; top: 300px; width: 68px; height: 67px; border: 2px solid #d9d9d9;
    background: var(--badge-grey); border-radius: 3px; text-align: center; color: var(--white);
  }
  .badge-fade { left: 971px; }
  .badge-life { left: 1051px; }
  .badge-number { font-size: 34px; font-weight: 400; line-height: 36px; margin-top: 2px; }
  .badge-number small { font-size: 5px; }
  .badge-title { font-size: 7px; margin-top: 4px; }
  .badge-fine { font-size: 3.6px; margin-top: 4px; }
  .badge-band { background: var(--white); color: var(--ink-dark); font-size: 13px; margin-top: 22px; line-height: 16px; }
  .badge-life .badge-title { margin-top: 4px; }
</style>
</head>
<body>
  <main class="poster">
    <div class="deck-photo" role="img" aria-label="Photo of a timber-clad elevated composite deck with a barbecue, wicker outdoor sofa with striped cushions, coffee table and dining setting overlooking trees"></div>

    <svg class="shapes" viewBox="0 0 1130 376" preserveAspectRatio="none" aria-hidden="true">
      <path d="M0 0 H372 C320 40 250 100 150 107 C90 110 40 109 0 109 Z" fill="#ffffff"/>
      <path d="M815 376 C900 372 950 300 1030 289 C1070 285 1110 284 1130 284 V376 Z" fill="#4d73a0"/>
    </svg>

    <div class="brand">
      <div class="brand-mark"></div>
      <div class="brand-name">Velmor Boards</div>
    </div>

    <div class="website">
      velmorboards.com.au
      <svg viewBox="0 0 24 24" fill="none" stroke="#fff" stroke-width="1.6">
        <circle cx="12" cy="12" r="10.5"/>
        <ellipse cx="12" cy="12" rx="4.5" ry="10.5"/>
        <path d="M1.5 12h21M3.5 6.5h17M3.5 17.5h17M12 1.5v21"/>
      </svg>
    </div>

    <div class="pill pill-maintenance"><strong>Ultra-Low</strong><span>Maintenance</span></div>
    <div class="pill pill-eco"><strong>Environmentally Friendly</strong><span>Made from Recycled Materials</span></div>

    <h1 class="headline"><em>50 YEAR</em><span>STAIN AND FADE WARRANTY</span></h1>

    <div class="pill pill-phone">
      <svg viewBox="0 0 24 24"><circle cx="12" cy="12" r="12" fill="#fff"/><path d="M8.2 5.5l2 2.6c.3.4.3.9 0 1.3l-1 1.2c.8 1.7 2.1 3 3.8 3.9l1.2-1c.4-.3.9-.3 1.3 0l2.6 2c.4.3.4.9.1 1.3l-1.1 1.3c-.5.5-1.2.7-1.9.5-4.3-1.3-7.6-4.6-8.9-8.9-.2-.7 0-1.4.5-1.9l1.3-1.1c.4-.3 1-.3 1.3.1z" fill="#4d73a0"/></svg>
      1300 482 937
    </div>

    <div class="badge badge-fade">
      <div class="badge-number">50<small>Year</small></div>
      <div class="badge-title">Stain and Fade</div>
      <div class="badge-fine">Limited Residential Warranty</div>
    </div>
    <div class="badge badge-life">
      <div class="badge-band">Lifetime</div>
      <div class="badge-title">Performance</div>
      <div class="badge-fine">Limited Residential Warranty</div>
    </div>
  </main>
</body>
</html>
```